Online Dating Website called WinkAtWheel.net

PLEASE CAN ALL PARTICIPATING DESIGNERS PLEASE SUBMIT ALL PAGES AS DETAILED IN THE ORIGINAL BRIEF BELOW WITHIN 48 HOURS TO AVOID WINKATWHEEL EXTENDING THE CONTEST FURTHER.

We have an online dating website that is 95% fully functional and now require an exciting and creative designer to help us create the best dating experience. We are looking for your ideas on a couple of our key pages. These are our landing, profile and search page. We already have a homepage that we are happy with and winning designers will look to build upon the foundations of the homepage and extend them through their designs.

The premise of the site is the idea that if you've ever seen someone out driving and wished you could communicate because you found them attractive, how would you? Well with WinkAtWheel.net you can. Just enter their vehicle registration number (license plate) in to the website in order to get in touch, flirt and develop a relationship. It also allows users to find each other based on other criteria. It acts as both a specialist service and a normal dating website.

The pages that require developing are 1) our landing page, this is the page users see when they first login to the site, it comprises various pieces of information but it's primary function is a live feed of events generated based on the users favourited profiles and interactions with the user. 2) The profile page is the page where users can edit their own information, given the nature of this page we are looking for a creative design that gives this page some flair. 3) Finally we are looking for ideas for our search page, this page needs to provide a list of users who meet the user's search requirements and display the profile of a selected user.
Updates

Project Deadline Extended
Reason: We've asked for certain pages in our brief to be designed and this still hasn't been done. We've contacted the designers that have currently submitted designs and requested this several times. We still await for this to happen.

Target Market(s)

Male or Female age 18+

Industry/Entity Type

Dating

Requirements
Must have
• Our must have feature is a designer with an open mind. The functionality of the site must be present, all we ask is for you to be creative with the layout. Think out side of the box, change the colours, the layout, and the background as you feel. Make it look current and appealing to the user.
Nice to have
• Theme's carried through from the home page
Should not have
• Do not include Comic Sans or Times New Roman font in your designs.

```html
<!DOCTYPE html>
<html lang="en">
<head>
<meta charset="utf-8">
<title>WinkAtWheel – Search</title>
<link href="https://fonts.googleapis.com/css2?family=Source+Sans+3:wght@400;600;700&display=swap" rel="stylesheet">
<style>
:root{
  --header-bg:#353535;
  --nav-text:#ffffff;
  --nav-pill:#17171c;
  --page-bg:#ffffff;
  --panel-border:#e2e2e2;
  --panel-bg:#ffffff;
  --card-body:#fbfbfb;
  --text-dark:#3a3a3a;
  --text-mid:#555555;
  --text-muted:#8a8a8a;
  --orange:#ff8a00;
  --pink:#e0407e;
  --green:#b2c512;
  --cyan:#00bfe0;
  --button-top:#a9abb0;
  --button-bottom:#7d8086;
  --footer-top:#444444;
  --footer-bottom:#1d1d1d;
  --footer-text:#e6e6e6;
  --chat-bg:#4a4a4a;
  --social-a:#3e5c98;
  --social-b:#4cb4e6;
  --social-c:#1c78b0;
}
*{box-sizing:border-box;margin:0;padding:0}
html,body{width:1200px;height:967px;overflow:hidden;background:var(--page-bg)}
body{font-family:"Source Sans 3",sans-serif;color:var(--text-dark)}
.page{position:relative;width:1200px;height:967px;overflow:hidden}

/* Header */
.site-header{position:absolute;left:0;top:0;width:1200px;height:111px;background:var(--header-bg);border-bottom:1px solid #222}
.brand{position:absolute;left:92px;top:34px;display:flex;align-items:center;gap:10px;color:#fff;font-size:36px;font-weight:400;letter-spacing:-0.5px}
.brand-dot{width:22px;height:22px;border-radius:50%;background:var(--pink)}
.main-nav{position:absolute;left:440px;top:39px;display:flex;align-items:center;height:43px}
.main-nav a{color:var(--nav-text);text-decoration:none;font-size:18px;padding:0 16px;line-height:43px;position:relative}
.main-nav a+a::before{content:"";position:absolute;left:0;top:13px;height:17px;border-left:1px solid #9a9a9a}
.main-nav a.is-active{background:var(--nav-pill);border-radius:22px;padding:0 18px;margin:0 10px}
.main-nav a.is-active::before,.main-nav a.is-active+a::before{display:none}

/* Feature cards */
.feature-card{position:absolute;border:1px solid var(--panel-border);border-radius:12px;background:var(--card-body);box-shadow:0 2px 3px rgba(0,0,0,.12);overflow:hidden;text-align:center}
.feature-card .card-top{position:absolute;left:0;top:0;width:100%;height:118px}
.feature-card .card-top svg.wave{position:absolute;left:0;top:0;width:100%;height:118px}
.feature-card .card-icon{position:absolute;left:50%;top:26px;transform:translateX(-50%)}
.feature-card h3{position:absolute;left:0;right:0;top:124px;font-size:22px;font-weight:400}
.feature-card p{position:absolute;left:18px;right:18px;top:155px;font-size:12.5px;line-height:17.5px;color:var(--text-muted)}
.card-find{left:81px;top:144px;width:213px;height:234px}
.card-find h3{color:var(--orange)}
.card-signup{left:87px;top:393px;width:207px;height:227px}
.card-signup h3{color:var(--pink)}
.card-connect{left:912px;top:150px;width:207px;height:227px}
.card-connect h3{color:var(--green)}
.card-dating{left:914px;top:391px;width:205px;height:225px}
.card-dating h3{color:var(--cyan)}

/* Panels */
.panel{position:absolute;border:1px solid var(--panel-border);border-radius:12px;background:var(--panel-bg);box-shadow:0 2px 3px rgba(0,0,0,.1);overflow:hidden}
.search-panel{left:314px;top:145px;width:572px;height:234px}
.panel-head{height:50px;padding-left:20px;line-height:50px;font-size:21px}
.search-panel .panel-head{background:linear-gradient(#f4f4f4,#d6d6d6);color:#555;border-bottom:1px solid #c9c9c9;border-radius:12px 12px 12px 12px;box-shadow:0 2px 2px rgba(0,0,0,.12)}
.field{position:absolute;height:34px;border:1px solid #d7d7d7;border-top:3px solid #e4e4e4;background:#fff;font-size:13.5px;color:#555;line-height:30px;padding-left:16px}
.field.select::after{content:"";position:absolute;right:10px;top:11px;border-left:6px solid transparent;border-right:6px solid transparent;border-top:9px solid #999}
.search-btn{position:absolute;left:393px;top:166px;width:132px;height:33px;border-radius:3px;background:linear-gradient(var(--button-top),var(--button-bottom));color:#fff;font-size:15px;font-weight:600;text-align:center;line-height:33px;border:1px solid #777}

.results-panel{left:314px;top:398px;width:572px;height:352px}
.results-panel .panel-head{background:linear-gradient(#fbfbfb,#efefef);color:var(--pink)}
.result{position:absolute;top:64px;width:120px}
.result .photo-frame{width:117px;height:110px;border-radius:10px;background:#f0f0f0;padding:6px}
.result .photo{width:105px;height:98px;border-radius:6px}
.result .name{margin-top:8px;font-size:13px;font-weight:600;color:#444;padding-left:5px}
.result .meta{font-size:13.5px;line-height:18px;color:#444;padding-left:5px}
.result .bio{margin-top:8px;font-size:12px;line-height:16px;color:var(--text-muted);padding-left:5px}

/* Chat tab */
.chat-tab{position:absolute;left:1149px;top:420px;width:51px;height:177px;background:var(--chat-bg);border:1px solid #2e2e2e;border-right:none;border-radius:4px 0 0 4px}
.chat-tab span{position:absolute;left:10px;top:120px;transform-origin:left top;transform:rotate(-90deg);color:#eee;font-weight:700;font-size:19px;white-space:nowrap;letter-spacing:.5px}

/* Footer */
.site-footer{position:absolute;left:0;top:811px;width:1200px;height:156px;background:linear-gradient(var(--footer-top),var(--footer-bottom));border-top:2px solid #8a8a8a}
.footer-col{position:absolute;top:16px;list-style:none}
.footer-col li{font-size:14px;color:var(--footer-text);line-height:28.5px}
.footer-col li::before{content:"» ";color:#bbb}
.footer-brand{position:absolute;left:846px;top:20px;color:#fff;font-size:34px;display:flex;align-items:center;gap:10px}
.footer-brand .brand-dot{background:#9c9c9c}
.copyright{position:absolute;right:115px;top:78px;text-align:right;font-size:14px;line-height:28px;color:var(--footer-text)}
.social{position:absolute;left:720px;top:87px;display:flex;gap:17px}
.social a{display:block;width:36px;height:36px;border-radius:3px}
.sr{position:absolute;width:1px;height:1px;overflow:hidden;clip:rect(0 0 0 0)}
</style>
</head>
<body>
<div class="page">

  <header class="site-header">
    <div class="brand">winkatwheel<span class="brand-dot"></span></div>
    <nav class="main-nav">
      <a href="#">Home</a><a href="#">Profile</a><a href="#">Messages</a><a href="#">Matches</a><a href="#" class="is-active">Search</a><a href="#">Support</a><a href="#">My Account</a>
    </nav>
  </header>

  <section class="feature-card card-find">
    <div class="card-top">
      <svg class="wave" viewBox="0 0 213 118" preserveAspectRatio="none"><path d="M0 0H213V100Q106 120 0 100Z" fill="var(--orange)"/></svg>
      <svg class="card-icon" width="62" height="62" viewBox="0 0 62 62"><circle cx="25" cy="25" r="18" fill="none" stroke="#fff" stroke-width="7"/><path d="M38 38L56 56" stroke="#fff" stroke-width="9" stroke-linecap="round"/><path d="M15 22a11 11 0 0 1 8-8" stroke="#fff" stroke-width="3" fill="none" stroke-linecap="round"/></svg>
    </div>
    <h3>Find Now</h3>
    <p>Vivamus porttitor, g, purus nisi eleifend libero, a tempus libero lectus feugiat felis diam</p>
  </section>

  <section class="feature-card card-signup">
    <div class="card-top">
      <svg class="wave" viewBox="0 0 207 118" preserveAspectRatio="none"><path d="M0 0H207V100Q103 84 0 100Z" fill="var(--pink)"/></svg>
      <svg class="card-icon" width="76" height="76" viewBox="0 0 76 76" style="top:18px"><path d="M22 54H16a13 13 0 0 1 0-26a20 20 0 0 1 38-6a14 14 0 0 1 6 32h-6" fill="none" stroke="#fff" stroke-width="6" stroke-linejoin="round"/><path d="M38 72V40M26 50l12-12l12 12" fill="none" stroke="#fff" stroke-width="7" stroke-linecap="round" stroke-linejoin="round"/></svg>
    </div>
    <h3>Sign Up</h3>
    <p>Vivamus porttitor, g, purus nisi eleifend libero, a tempus libero lectus feugiat felis diam</p>
  </section>

  <section class="panel search-panel">
    <div class="panel-head">Search Your Match</div>
    <div class="field select" style="left:25px;top:69px;width:231px">I am a..</div>
    <div class="field select" style="left:284px;top:69px;width:231px">Aged between</div>
    <div class="field" style="left:25px;top:119px;width:231px">Colour</div>
    <div class="field" style="left:284px;top:119px;width:231px">Location</div>
    <div class="field select" style="left:25px;top:163px;width:231px">My Postcode</div>
    <div class="search-btn">SEARCH NOW</div>
  </section>

  <section class="panel results-panel">
    <div class="panel-head">Search Results</div>
    <div class="result" style="left:25px">
      <div class="photo-frame"><div class="photo" role="img" aria-label="Member profile photo" style="background:linear-gradient(#c9c4bf,#8e7a6c)"></div></div>
      <div class="name">Person Name</div><div class="meta">Age 26<br>Location</div>
      <div class="bio">Mauris vel lacus vitae felis vestibulum volutpat.</div>
    </div>
    <div class="result" style="left:159px">
      <div class="photo-frame"><div class="photo" role="img" aria-label="Member profile photo" style="background:linear-gradient(#eaeaea,#b59e8c)"></div></div>
      <div class="name">Person Name</div><div class="meta">Age 26<br>Location</div>
      <div class="bio">Mauris vel lacus vitae felis vestibulum volutpat.</div>
    </div>
    <div class="result" style="left:294px;top:68px">
      <div class="photo-frame"><div class="photo" role="img" aria-label="Member profile photo" style="background:linear-gradient(#f1f1ee,#b89c80)"></div></div>
      <div class="name">Person Name</div><div class="meta">Age 26<br>Location</div>
      <div class="bio">Mauris vel lacus vitae felis vestibulum volutpat.</div>
    </div>
    <div class="result" style="left:427px;top:68px">
      <div class="photo-frame"><div class="photo" role="img" aria-label="Member profile photo" style="background:linear-gradient(#d8d8d6,#a88d7c)"></div></div>
      <div class="name">Person Name</div><div class="meta">Age 26<br>Location</div>
      <div class="bio">Mauris vel lacus vitae felis vestibulum volutpat.</div>
    </div>
  </section>

  <section class="feature-card card-connect">
    <div class="card-top">
      <svg class="wave" viewBox="0 0 207 118" preserveAspectRatio="none"><path d="M0 0H207V96Q103 112 0 96Z" fill="var(--green)"/></svg>
      <svg class="card-icon" width="76" height="64" viewBox="0 0 76 64" style="top:24px;left:53%"><path d="M34 58L10 34A14 14 0 0 1 34 12A14 14 0 0 1 58 28" fill="none" stroke="#fff" stroke-width="6" stroke-linejoin="round"/><circle cx="54" cy="44" r="16" fill="#fff"/><path d="M54 35V53M45 44H63" stroke="var(--green)" stroke-width="5"/></svg>
    </div>
    <h3>Get Connect</h3>
    <p>Vivamus porttitor, g, purus nisi eleifend libero, a tempus libero lectus feugiat felis diam</p>
  </section>

  <section class="feature-card card-dating">
    <div class="card-top">
      <svg class="wave" viewBox="0 0 205 118" preserveAspectRatio="none"><path d="M0 0H205V100Q102 86 0 100Z" fill="var(--cyan)"/></svg>
      <svg class="card-icon" width="68" height="68" viewBox="0 0 68 68" style="top:18px"><circle cx="34" cy="34" r="30" fill="none" stroke="#fff" stroke-width="5"/><path d="M34 50L20 36A8 8 0 0 1 34 24A8 8 0 0 1 48 36Z" fill="#fff"/></svg>
    </div>
    <h3>Dating</h3>
    <p>Vivamus porttitor, g, purus nisi eleifend libero, a tempus libero lectus feugiat felis diam</p>
  </section>

  <aside class="chat-tab">
    <span>OPEN CHAT</span>
    <svg width="32" height="26" viewBox="0 0 32 26" style="position:absolute;left:9px;top:136px"><path d="M2 3h18v11H9l-5 4v-4H2z" fill="#ddd"/><path d="M13 10h17v11h-2v4l-5-4H13z" fill="#eee"/></svg>
  </aside>

  <footer class="site-footer">
    <ul class="footer-col" style="left:116px"><li>Home</li><li>Mobile Site</li><li>Friendbook</li><li>Chirper</li></ul>
    <ul class="footer-col" style="left:259px"><li>General Conditions</li><li>Terms &amp; Conditions</li><li>Privacy Statement</li><li>Cookies Information</li></ul>
    <ul class="footer-col" style="left:461px"><li>Contact us</li><li>FAQ's &amp; Help</li><li>Safe Dating Advice</li><li>Pricing Details</li></ul>
    <div class="footer-brand">winkatwheel<span class="brand-dot"></span></div>
    <div class="social">
      <a href="#" style="background:var(--social-a)"><span class="sr">Friendbook</span></a>
      <a href="#" style="background:var(--social-b)"><span class="sr">Chirper</span></a>
      <a href="#" style="background:var(--social-c)"><span class="sr">Linkwork</span></a>
    </div>
    <div class="copyright">Copyright ©&nbsp; 2013&nbsp;&nbsp; Wink At Wheel<br>All rights reserved.</div>
  </footer>

</div>
</body>
</html>
```